Coldmerrow Brochure & Fact Sheet

We need a brochure designed that we will distribute both digitally (PDF) and also have printed. We our an IT company and would like the creative to reflect our brand and industry. All content is written and ready to go. We need each page of the brochure provided as an individual file so we can arrange the pages as needed.

```html
<!DOCTYPE html>
<html lang="en">
<head>
<meta charset="utf-8">
<title>Coldmerrow Brochure &amp; Fact Sheet</title>
<link rel="stylesheet" href="https://fonts.googleapis.com/css2?family=Open+Sans:ital,wght@0,300;0,400;0,600;0,700;1,400&display=swap">
<style>
:root{
  --bg:#e6e6e6;
  --paper:#ffffff;
  --ink:#1a1a1a;
  --muted:#555555;
  --dark:#1c1c1c;
  --black:#000000;
  --accent:#1565e0;
  --cell:#e8e8e8;
  --band:#efefef;
  --note:#7a7a7a;
  --icon-fill:#dde4ee;
}
*{margin:0;padding:0;box-sizing:border-box}
html,body{width:1200px;height:1200px;overflow:hidden;background:var(--bg);font-family:"Open Sans",sans-serif;color:var(--ink)}
.canvas{position:relative;width:1200px;height:1200px}
.page{position:absolute;width:416px;height:538px;background:var(--paper);box-shadow:0 2px 6px rgba(0,0,0,.12);overflow:hidden}
.page--cover{left:136px;top:58px}
.page--facts{left:595px;top:58px}
.page--services{left:136px;top:621px}
.abs{position:absolute}
.brand{display:flex;align-items:center;gap:5px;font-weight:700;letter-spacing:-.02em}
.brand__dot{border-radius:50%;background:currentColor;flex:none}

/* cover */
.cover__photo{left:0;top:0;width:416px;height:270px;background:linear-gradient(180deg,#cfc7bd 0%,#d9d3cb 40%,#ece9e5 72%,#ffffff 100%)}
.cover__brand{left:0;width:416px;top:42px;justify-content:center;font-size:17px;color:#1a1a1a}
.cover__brand .brand__dot{width:10px;height:10px}
.cover__title{left:36px;top:252px;width:360px;font-weight:300;font-size:20.5px;line-height:21px;letter-spacing:-.03em}
.cover__rule{left:36px;top:304px;width:64px;height:3px;background:var(--accent)}
.cover__body{left:36px;top:321px;width:340px;font-size:7.1px;line-height:9.3px;text-align:justify}
.cover__body p{margin-bottom:9.3px}
.footer{left:0;top:502px;width:416px;height:36px;display:flex;align-items:center;justify-content:space-between;padding:0 34px}
.footer--dark{background:var(--black);color:#fff}
.footer--light{background:var(--band);color:var(--ink);padding:0 26px 0 20px}
.footer__url{font-size:6.2px;font-style:italic}
.footer .brand{font-size:9.5px}
.footer .brand__dot{width:7px;height:7px}

/* facts */
.facts__head{left:34px;top:28px;display:flex;align-items:center;font-size:26px;font-weight:300;letter-spacing:-.02em;color:var(--ink)}
.facts__head .brand__dot{width:38px;height:38px;margin-right:8px;color:var(--black)}
.fact{position:absolute;left:61px;width:286px}
.fact__label{position:absolute;left:0;top:0;width:126px;border-top:1.5px solid #e3e3e3;padding:6px 0 0 13px;font-size:6.8px}
.fact__label::before{content:"";position:absolute;left:-1px;top:-4px;width:6px;height:6px;border-radius:50%;background:var(--accent)}
.fact__value{position:absolute;left:126px;top:0;width:160px;background:var(--cell);padding:6px 4px 6px 16px;font-size:6.6px;line-height:10px;font-weight:700;white-space:nowrap;letter-spacing:-.01em}
.fact__value .plain{font-weight:400}
.facts__rule{left:61px;top:365px;width:286px;height:1.5px;background:#e3e3e3}
.facts__col{top:375px;width:150px}
.facts__col h3{font-weight:400;font-size:13px;letter-spacing:-.02em;margin-bottom:5px}
.facts__col li{list-style:none;font-size:6.3px;line-height:8.8px;color:var(--muted)}
.facts__col li.strong{font-weight:700;color:var(--ink)}

/* services */
.services__hero{left:0;top:0;width:416px;height:184px;background:var(--dark);color:#fff}
.services__mark{left:38px;top:42px;width:50px;height:50px;border-radius:50%;background:#fff}
.services__title{left:99px;top:32px;font-weight:300;font-size:25px;line-height:29px;letter-spacing:-.02em}
.services__intro{left:36px;top:112px;width:352px;font-size:7.1px;line-height:9.3px}
.services__sub{left:35px;top:198px;font-weight:600;font-size:12.5px;letter-spacing:-.01em}
.service{position:absolute;top:243px;width:154px}
.service__icon{width:62px;height:62px;border-radius:8px;background:var(--icon-fill)}
.service h4{margin-top:17px;font-weight:400;font-size:12.5px;letter-spacing:-.02em}
.service p{margin-top:5px;font-size:6.4px;line-height:9.3px;text-align:justify;color:#333}

/* note */
.note{left:606px;top:722px;width:560px;font-size:58px;line-height:60px;letter-spacing:-.065em;color:var(--note);font-weight:400}
</style>
</head>
<body>
<main class="canvas">

  <!-- Page 1: cover -->
  <section class="page page--cover">
    <div class="abs cover__photo" role="img" aria-label="Photo of hands typing on a laptop at a bright desk with a notebook"></div>
    <div class="abs brand cover__brand"><span class="brand__dot"></span>coldmerrow</div>
    <h1 class="abs cover__title">Harness the Potential of Technology with Coldmerrow</h1>
    <div class="abs cover__rule"></div>
    <div class="abs cover__body">
      <p>We believe that technology has the potential to develop industry leaders, but it’s not a fail-safe and doesn’t come with a success guarantee. In short, technology alone is not enough to produce the results you’re looking for. It requires experience solving complex problems and trusted advice that’s based on your unique background, is authentic in nature, and actionable in practice.</p>
      <p>&nbsp;It’s when you combine a robust tech platform with smart, informed ideas and customized IT strategies, that you start to see results. <b>And that’s why we’re here.</b></p>
      <p>At Coldmerrow, our team has a reputation for being innovative, proactive, and easy to work with. We see customers as true partners and advisors in the process, and rather than rushing ahead blindly without thought and intention, we move forward with care, meaning each and every step along the way is rooted in understanding, clarity, and enablement. At the end of the day, we want you to walk away with &nbsp;a set of personalized IT strategies that you <b>understand, value, and feel empowered</b> to implement.</p>
    </div>
    <footer class="abs footer footer--dark">
      <span class="footer__url">www.coldmerrow.com</span>
      <span class="brand"><span class="brand__dot"></span>coldmerrow</span>
    </footer>
  </section>

  <!-- Page 2: facts -->
  <section class="page page--facts">
    <h2 class="abs facts__head"><span class="brand__dot"></span>Coldmerrow Facts</h2>

    <div class="fact" style="top:111px">
      <div class="fact__label">Established</div>
      <div class="fact__value" style="height:21px">2000</div>
    </div>
    <div class="fact" style="top:151px">
      <div class="fact__label">Headquarters</div>
      <div class="fact__value" style="height:31px;padding-top:5px;line-height:9px">418 Larkfield Ave. NW<br>Halbrook, MI 49260</div>
    </div>
    <div class="fact" style="top:191px">
      <div class="fact__label">Headquarters</div>
      <div class="fact__value" style="height:51px;padding-top:5px">
        <span class="plain">Dean Harlow,</span> CEO<br>
        <span class="plain">Paul Brinkerhoff,</span> COO<br>
        <span class="plain">Owen Castell,</span> VP Digital Transformation<br>
        <span class="plain">Rick Tannery,</span> VP Sales &amp; Marketing
      </div>
    </div>
    <div class="fact" style="top:253px">
      <div class="fact__label">Team Members</div>
      <div class="fact__value" style="height:20px">25</div>
    </div>
    <div class="fact" style="top:282px">
      <div class="fact__label">Combined Staff Experience</div>
      <div class="fact__value" style="height:20px">85+ Years</div>
    </div>
    <div class="fact" style="top:312px">
      <div class="fact__label">Core Services</div>
      <div class="fact__value" style="height:42px">Full Service Managed IT Services<br>Webforge Website Development<br>IT Consulting</div>
    </div>
    <div class="abs facts__rule"></div>

    <div class="abs facts__col" style="left:61px">
      <h3>Accolades</h3>
      <ul>
        <li class="strong">Lakeshore 100 Best &amp; Brightest</li>
        <li class="strong">MSP Leaders 500</li>
        <li>Webforge Website of the Year 2013</li>
        <li>Webforge Website of the Year 2014</li>
        <li>Webforge Website of the Year 2015</li>
        <li>Webforge Website of the Year 2017</li>
        <li>Webforge Partner of the Year 2016</li>
      </ul>
    </div>
    <div class="abs facts__col" style="left:204px">
      <h3>Certifications</h3>
      <ul>
        <li>Webforge Elite Partner</li>
        <li>Northgrid Certified Gold Partner</li>
        <li>Virtuon Certified Partner</li>
        <li>Storalis Certified Partner</li>
        <li>Backvale Certified Partner</li>
        <li>Gatemark Certified Partner</li>
      </ul>
    </div>

    <footer class="abs footer footer--light">
      <span class="footer__url">www.coldmerrow.com</span>
      <span class="brand"><span class="brand__dot"></span>coldmerrow</span>
    </footer>
  </section>

  <!-- Page 3: managed services -->
  <section class="page page--services">
    <div class="abs services__hero">
      <div class="abs services__mark"></div>
      <h2 class="abs services__title">Coldmerrow<br>Managed IT Services</h2>
      <p class="abs services__intro">Managed Services by Coldmerrow delivers proactive monitoring, maintenance, security and IT support for small and medium size business infrastructures, applications and cloud solutions. Based in West Michigan, we provide a hands-on service approach and design end-to-end IT solutions that help your company grow efficiently, remain flexible, and maintain a lean IT operation. We employ a dedicated team of infrastructure experts that ensure your business operations are running smoothly, with no downtime, 24 hours a day. IT shouldn’t be a disruption, but a reliable tool, and it’s our job to make that happen.</p>
    </div>
    <h3 class="abs services__sub">Our Managed IT Services Approach</h3>

    <div class="service" style="left:35px">
      <div class="service__icon" role="img" aria-label="Line illustration representing cloud infrastructure"></div>
      <h4>Infrastructure</h4>
      <p>Managed Services by Coldmerrow delivers proactive monitoring, maintenance, security and IT support for small and medium size business infrastructures, applications and cloud solutions. Based in West Michigan, we provide a hands-on service approach and design end-to-end IT solutions that help your company grow efficiently, remain flexible, and maintain a lean IT operation. We employ a dedicated team of infrastructure experts that ensure your business operations are running smoothly, with no downtime, 24 hours a day. IT shouldn’t be a disruption, but a reliable tool, and it’s our job to make that happen.</p>
    </div>

    <div class="service" style="left:220px">
      <div class="service__icon" role="img" aria-label="Line illustration representing network security"></div>
      <h4>Security</h4>
      <p>Our security services include endpoint security, network security, cloud security and policy management. We focus on protecting our partners from today’s sophisticated cyber security threats by helping them outline, implement and maintain customized security policies and procedures. We stay abreast of all security developments and threats and strive to educate everyone on how to protect themselves both personally and professionally.</p>
    </div>

    <footer class="abs footer footer--light">
      <span class="footer__url">www.coldmerrow.com</span>
      <span class="brand"><span class="brand__dot"></span>coldmerrow</span>
    </footer>
  </section>

  <p class="abs note">Dear project manager, I’m working on other pages. I saw the contest late. Thank you.</p>

</main>
</body>
</html>
```